Web Design Project

blaze guard safety & solutions needs a new web design to go with its new logo design

we provide services such as instillation of fire sprinklers, fire hydrants , fire hose reels as well as fire extinguishers and fire blankets.

we can service these as well and also do the preventitave maintaince of these too.

we can do flow testing of sprinklers,hydrants & hosereels and test back flow prevention devices as well

old page is bgss-example.com.au

Industry/Entity Type

Defence

```html
<!DOCTYPE html>
<html lang="en">
<head>
<meta charset="utf-8">
<title>Blaze Guard Safety &amp; Solutions</title>
<link rel="stylesheet" href="https://fonts.googleapis.com/css2?family=Archivo+Narrow:ital,wght@0,400;0,600;0,700;1,400;1,600&family=Arimo:wght@400;700&display=swap">
<style>
:root{
  --red:#c8151b;
  --deep-red:#6e0204;
  --orange:#f7941d;
  --panel:#0d0d0d;
  --panel-edge:#2a2a2a;
  --body-text:#9a9a9a;
  --muted:#5a5a5a;
  --ink:#333;
  --white:#fff;
}
*{box-sizing:border-box;margin:0;padding:0}
html,body{width:1200px;height:1047px;overflow:hidden}
body{position:relative;font-family:"Arimo",Arial,sans-serif;
  background:linear-gradient(180deg,#7a0305 130px,#b3090d 400px,#8a0406 700px,#d2420c 940px,#000 985px)}
.top-strip{position:absolute;left:0;top:0;width:1200px;height:16px;background:#d9d9d9}
.site-header{position:absolute;left:0;top:16px;width:1200px;height:114px;
  background:linear-gradient(180deg,#ffffff,#eaeaea)}
.brand{position:absolute;left:100px;top:30px;display:flex;align-items:center;gap:10px}
.brand-mark{width:22px;height:22px;background:var(--red)}
.brand-name{font-family:"Archivo Narrow",sans-serif;font-weight:700;font-size:21px;color:var(--red);text-transform:uppercase;line-height:1.05;width:220px}
.tagline{position:absolute;left:398px;top:52px;font-family:"Archivo Narrow",sans-serif;font-style:italic;font-weight:600;font-size:27px;color:#6b6b6b;white-space:nowrap}
.hotline{position:absolute;left:783px;top:18px;width:340px;height:90px;white-space:nowrap}
.hotline-247{position:absolute;left:0;top:14px;font-family:"Archivo Narrow",sans-serif;font-style:italic;font-size:64px;color:var(--red);line-height:1}
.hotline-call{position:absolute;left:139px;top:4px;font-family:"Archivo Narrow",sans-serif;font-weight:700;font-size:27px;color:var(--ink);line-height:1.1}
.hotline-label{position:absolute;left:112px;top:34px;font-family:"Archivo Narrow",sans-serif;font-style:italic;font-size:33px;color:#555;line-height:1.1}
.main-panel{position:absolute;left:91px;top:132px;width:1020px;height:878px;background:var(--panel);border-radius:20px 20px 0 0;box-shadow:0 0 10px rgba(0,0,0,.6)}
.main-nav{position:absolute;left:0;top:0;width:1020px;height:65px;border-radius:20px 20px 0 0;
  background:linear-gradient(180deg,#3b3b3b,#111 55%,#000)}
.main-nav a{position:absolute;top:24px;font-size:17px;color:var(--white);text-decoration:none}
.main-nav a.current{color:var(--orange)}
.hero{position:absolute;left:26px;top:74px;width:970px;height:337px;border-radius:20px;
  background:radial-gradient(ellipse at 30% 40%,#ffffff,#e4e4e4 55%,#a9a9a9)}
.hero-copy{position:absolute;left:62px;top:60px;font-family:"Archivo Narrow",sans-serif;color:#2e2e2e}
.hero-line1{font-size:48px;font-weight:600;line-height:1}
.hero-line1 .accent{color:var(--orange);font-size:62px}
.hero-line2{display:flex;align-items:flex-end;margin-top:4px}
.hero-line2 .lead{font-size:34px;font-weight:600;line-height:1.1;text-align:right}
.hero-line2 .big{font-size:92px;font-weight:700;color:#b30f14;line-height:.9;margin-left:6px}
.hero-note{font-size:17px;margin-top:14px;font-weight:600}
.hero-visual{position:absolute;left:670px;top:20px;width:280px;height:300px;border-radius:14px;
  background:radial-gradient(circle at 60% 50%,#d8262b,#9d0e12 45%,rgba(200,200,200,0) 72%)}
.features{position:absolute;left:26px;top:430px;width:970px;height:72px;border-radius:18px;
  background:linear-gradient(180deg,#ffffff,#dcdcdc)}
.feature{position:absolute;top:21px;display:flex;align-items:center;gap:10px;font-family:"Archivo Narrow",sans-serif;font-size:26px;line-height:30px;color:#1a1a1a;white-space:nowrap}
.feature svg{display:block}
.welcome{position:absolute;left:26px;top:540px;width:660px}
.welcome h1{display:flex;align-items:center;gap:10px;font-family:"Archivo Narrow",sans-serif;font-weight:400;font-size:26px;color:var(--white);white-space:nowrap}
.welcome p{font-size:14.5px;line-height:18px;color:var(--body-text);margin-top:16px}
.welcome h1 + p{margin-top:20px}
.news{position:absolute;left:747px;top:543px;width:249px;height:293px;border-radius:16px;background:#1b1b1b}
.news h2{height:62px;border-radius:16px 16px 0 0;background:linear-gradient(180deg,#3a3a3a,#202020);
  font-family:"Archivo Narrow",sans-serif;font-weight:400;font-size:28px;color:var(--white);text-align:center;padding-top:13px}
.news-body{padding:22px 20px 0;font-size:13px;color:var(--muted)}
.news-title{font-weight:700;color:#6e6e6e}
.news-title span{color:#e02020}
.news-date{margin-top:20px;font-size:14px}
.news-text{margin-top:16px;line-height:16px;text-align:justify}
.news-more{display:block;text-align:right;margin-top:12px;color:#c0181d;text-decoration:none}
.site-footer{position:absolute;left:0;top:1010px;width:1200px;height:37px;background:#000;
  font-size:12px;color:#3d3d3d;text-align:center;padding-top:14px}
</style>
</head>
<body>
<div class="top-strip"></div>
<header class="site-header">
  <div class="brand"><span class="brand-mark"></span><span class="brand-name">Blaze Guard Safety &amp; Solutions</span></div>
  <p class="tagline">Your best defence against fire'</p>
  <div class="hotline">
    <span class="hotline-247">24/7</span>
    <span class="hotline-call">CALL : 0491570156</span>
    <span class="hotline-label">Emergency service</span>
  </div>
</header>

<main class="main-panel">
  <nav class="main-nav">
    <a class="current" href="#" style="left:63px">Home</a>
    <a href="#" style="left:257px">Service</a>
    <a href="#" style="left:404px">Testing</a>
    <a href="#" style="left:586px">Products</a>
    <a href="#" style="left:730px">FAQ'S</a>
    <a href="#" style="left:881px">Contact Us</a>
  </nav>

  <section class="hero">
    <div class="hero-copy">
      <div class="hero-line1">Fire service assets and <span class="accent">provide a</span></div>
      <div class="hero-line2">
        <div class="lead">full quotation on a<br>service contract</div>
        <div class="big">12 month</div>
      </div>
      <p class="hero-note">At Blaze Guard we can supply and install portable fire protection to suit you needs.</p>
    </div>
    <div class="hero-visual" role="img" aria-label="Red fire extinguisher, hose reel and first aid kit"></div>
  </section>

  <section class="features">
    <div class="feature" style="left:34px">
      <svg width="16" height="30" viewBox="0 0 16 30"><rect x="3" y="8" width="10" height="21" rx="4" fill="#c8151b"/><rect x="5" y="2" width="6" height="6" fill="#333"/></svg>
      Fire extinguishers
    </div>
    <div class="feature" style="left:370px">
      <svg width="30" height="24" viewBox="0 0 30 24"><rect x="1" y="3" width="28" height="20" rx="3" fill="#c8151b"/><path d="M12 8h6v4h4v4h-4v4h-6v-4H8v-4h4z" fill="#fff"/></svg>
      Fire blankets
    </div>
    <div class="feature" style="left:668px">
      <svg width="26" height="26" viewBox="0 0 26 26"><circle cx="13" cy="13" r="11" fill="#c8151b"/><circle cx="13" cy="13" r="4" fill="#333"/></svg>
      Fire Hose reels &amp; hydrants
    </div>
  </section>

  <section class="welcome">
    <h1><svg width="18" height="30" viewBox="0 0 18 30"><path d="M9 1C12 8 17 12 17 20a8 8 0 0 1-16 0C1 13 7 10 9 1z" fill="#f7941d"/><path d="M9 12c2 4 4 6 4 9a4 4 0 0 1-8 0c0-3 3-5 4-9z" fill="#c8151b"/></svg>Welcome to our Blaze Guard Safety &amp; Solutions Pty Ltd!</h1>
    <p>At Blaze Guard we believe that no matter how large or small your business is we can help you with the design, installation and the maintenance of your system to the standard which it was designed to.</p>
    <p>Blaze Guard is a fire protection company situated on the Central Coast of NSW and is currently servicing the Sydney, Central Coast and Hunter areas, We are always looking for new clients who are not happy with there current service providers and are looking for a competitive priced alternative. Blaze Guard will come to your site and assess your fire service assets and provide a full quotation on a 12 month service contract.</p>
    <p>Blaze Guard can also supply quotations for any alterations to your Sprinklers,Hydrants &amp; Hose reel systems along with your fire detection and emergency lighting.</p>
    <p>Blaze Guard is a owner operated business, so our reputation is our guarantee to do the best job we possibly can.</p>
  </section>

  <aside class="news">
    <h2>Blaze Guard News</h2>
    <div class="news-body">
      <p class="news-title">Celebrating <span>60 Years!</span></p>
      <p class="news-date">July 21, 2009</p>
      <p class="news-text">Blaze Guard is celebrating its 60th year! 2009 marks our sixth decade of meeting and exce</p>
      <a class="news-more" href="#">Read More...</a>
    </div>
  </aside>
</main>

<footer class="site-footer">Copyright 2010 BGSS-EXAMPLE.COM.AU All Rights Reserved.</footer>
</body>
</html>
```